Franchise Vacation Rental Company Website

We are looking for fresh, new and creative design ideas to help enhance this site. We are a vacation rental company that is starting a new franchise business. This will be our home franchise page, and will need to appeal to franchise candidates as well as travelers looking for vacation homes in our current locations.

Business

```html
<!DOCTYPE html>
<html lang="en">
<head>
<meta charset="utf-8">
<title>Fair Havens – Find Your Haven</title>
<link href="https://fonts.googleapis.com/css2?family=Signika:wght@400;600&family=PT+Sans:ital,wght@0,400;0,700;1,700&display=swap" rel="stylesheet">
<style>
:root{
  --blue-dark:#17569d;
  --blue:#1f78c4;
  --blue-foot:#4a90cf;
  --green:#8dc63f;
  --grey-band:#e4e4e4;
  --grey-text:#333;
  --grey-soft:#666;
  --line:#d6d6d6;
  --white:#fff;
}
*{margin:0;padding:0;box-sizing:border-box}
html,body{width:1050px;height:1200px;overflow:hidden;background:#fff}
body{font-family:"PT Sans",sans-serif;color:var(--grey-text)}
.page{position:relative;width:1200px;height:1372px;transform:scale(.875);transform-origin:0 0}
.abs{position:absolute}
.head{left:0;top:0;width:1200px;height:112px;background:linear-gradient(180deg,var(--blue-dark),#2384cd)}
.brand{left:172px;top:26px;font-family:"Signika",sans-serif;font-weight:400;font-size:46px;color:var(--white);display:flex;align-items:center;gap:12px}
.brand i{display:block;width:16px;height:16px;border-radius:50%;background:var(--green)}
.mail{right:172px;top:22px;font-size:13px;font-weight:700;color:var(--white);display:flex;gap:6px;align-items:center}
.phone{right:172px;top:45px;font-size:28px;font-weight:700;color:var(--white);letter-spacing:1px;text-align:right;line-height:1}
.phone small{display:block;font-size:13px;letter-spacing:1px;margin-top:2px}
.nav{left:0;top:112px;width:1200px;height:43px;background:linear-gradient(180deg,#3a8fd6,#1f6db5);border-top:1px solid #6aaee6}
.nav .home{position:absolute;left:172px;top:0;width:61px;height:43px;background:#1a5d9a;border-top:3px solid var(--green);display:flex;align-items:center;justify-content:center}
.nav a{position:absolute;top:15px;font-size:11px;font-weight:700;color:var(--white);text-decoration:none;text-transform:uppercase}
.find{left:0;top:155px;width:1200px;height:61px;background:#fff;border-bottom:1px solid var(--line)}
.find h2{position:absolute;left:200px;top:24px;font-family:"Signika",sans-serif;font-weight:600;font-size:21px;color:var(--blue)}
.find .hint{position:absolute;left:417px;top:35px;font-size:10px;color:var(--grey-soft)}
.social{position:absolute;top:30px;width:20px;height:20px;border-radius:2px}
.band{left:0;top:216px;width:1200px;height:424px;background:var(--grey-band)}
.tile{position:absolute;width:256px;height:169px;display:flex;align-items:flex-end;justify-content:center;padding-bottom:18px;color:var(--white);font-size:13px}
.join{position:absolute;left:751px;top:438px;width:256px;height:169px;background:linear-gradient(180deg,#3d4a4f,#1e2b30);border:2px solid #2a7fc9;box-shadow:0 0 6px rgba(0,0,0,.4);text-align:center;color:var(--white)}
.join h3{font-family:"Signika",sans-serif;font-weight:400;font-size:22px;color:#2a8ee0;margin-top:34px}
.join p{font-size:11px;font-weight:700;line-height:15px;margin-top:6px}
.join span{display:block;margin:10px auto 0;width:157px;height:26px;background:#fff;color:var(--blue);font-size:11px;font-weight:700;line-height:26px}
.main{left:172px;top:640px;width:856px;height:538px;background:#fff;box-shadow:0 1px 3px rgba(0,0,0,.2)}
.intro h1{position:absolute;left:194px;top:672px;font-family:"Signika",sans-serif;font-weight:600;font-size:24px;line-height:30px;color:var(--blue)}
.intro h4{position:absolute;left:194px;top:735px;font-family:"Signika",sans-serif;font-weight:600;font-size:16px;color:var(--green)}
.intro .copy{position:absolute;left:194px;top:772px;width:448px;font-size:14px;line-height:16.5px;color:var(--grey-text)}
.copy p{margin-bottom:17px}
.signup{left:668px;top:677px;font-family:"Signika",sans-serif;font-weight:600;font-size:13px;color:var(--blue)}
.email{left:665px;top:704px;width:230px;height:29px;border:1px solid #ccc;font-size:10px;color:#999;padding:8px 10px}
.btn{left:900px;top:704px;width:107px;height:29px;border:1px solid #aaa;font-size:10px;font-weight:700;color:var(--grey-soft);text-align:center;line-height:27px}
.card{position:absolute;left:666px;width:341px;border:1px solid #e4e4e4;background:linear-gradient(180deg,#fff,#f7f7f7)}
.card.lift{box-shadow:0 1px 4px rgba(0,0,0,.25)}
.card .ico{position:absolute;left:15px;top:13px;width:58px;height:58px;border-radius:50%;background:var(--green);display:flex;align-items:center;justify-content:center}
.card h3{position:absolute;left:85px;top:12px;font-family:"Signika",sans-serif;font-weight:600;font-size:17px;color:var(--blue)}
.card h3 em{font-family:"PT Sans",sans-serif;font-weight:700}
.card p{position:absolute;left:85px;top:36px;width:250px;font-size:14px;line-height:16.5px;color:var(--grey-text)}
.card a{position:absolute;left:85px;font-size:12px;font-weight:700;color:var(--blue);text-decoration:none}
.foot{left:172px;top:1198px;width:856px;height:117px;background:#fff}
.bar{position:absolute;top:0;height:4px;width:285px}
.col{position:absolute;top:22px;font-size:11px;line-height:16px;color:var(--grey-text)}
.col h5{font-family:"Signika",sans-serif;font-weight:600;font-size:17px;color:var(--blue);margin-bottom:6px}
.col u{color:var(--blue)}
.legal{left:172px;top:1315px;width:856px;height:56px;background:var(--blue-foot);color:var(--white);font-size:10px;line-height:16px;padding:12px 18px}
.legal .dot{position:absolute;top:18px;width:22px;height:22px;border-radius:50%;background:#6ea8dc}
</style>
</head>
<body>
<div class="page">
  <header class="abs head">
    <div class="abs brand"><i></i>Fair Havens</div>
    <div class="abs mail">
      <svg width="14" height="10" viewBox="0 0 14 10"><rect x=".5" y=".5" width="13" height="9" fill="none" stroke="#fff"/><path d="M.5 .5 7 6 13.5 .5" fill="none" stroke="#fff"/></svg>
      info@fairhavens-stays.com</div>
    <div class="abs phone">1.855.FAIR.HVN<small>(1.855.324.7486)</small></div>
  </header>

  <nav class="abs nav">
    <div class="home"><svg width="18" height="16" viewBox="0 0 18 16"><path d="M9 1 1 8h2v7h4v-4h4v4h4V8h2z" fill="#8dc63f"/></svg></div>
    <a style="left:266px">See our havens</a>
    <a style="left:418px">Franchise information</a>
    <a style="left:589px">Our philosophy</a>
    <a style="left:716px">List your property</a>
    <a style="left:862px">Contact us</a>
    <a style="left:965px">News</a>
  </nav>

  <section class="abs find">
    <svg style="position:absolute;left:176px;top:26px" width="16" height="22" viewBox="0 0 16 22"><path d="M8 1a7 7 0 0 0-7 7c0 5 7 13 7 13s7-8 7-13a7 7 0 0 0-7-7z" fill="none" stroke="#8dc63f" stroke-width="2.4"/></svg>
    <h2>Find Your Fair Haven!</h2>
    <svg style="position:absolute;left:402px;top:36px" width="8" height="10" viewBox="0 0 8 10"><path d="M1 1l5 4-5 4" fill="none" stroke="#8dc63f" stroke-width="2"/></svg>
    <span class="hint">Choose one of the locations to began your search</span>
    <span class="social" style="left:911px;background:#3b5998"></span>
    <span class="social" style="left:940px;background:#1da1f2"></span>
    <span class="social" style="left:969px;width:32px;border:1px solid #d23;background:#fff"></span>
    <span class="social" style="left:1005px;width:20px;border:1px solid #ccc;background:#fff;font-size:10px;color:#666;text-align:center;line-height:18px">8</span>
  </section>

  <section class="abs band">
    <div class="tile" role="img" aria-label="Patio table with umbrella overlooking water" style="left:195px;top:32px;background:linear-gradient(180deg,#7f94ab,#4f6a3c 60%,#2f3a2a)">Maryland Eastern Shore</div>
    <div class="tile" role="img" aria-label="Harbor with moored boats" style="left:473px;top:32px;background:linear-gradient(180deg,#8ea0b6,#6a7a88 55%,#2c3844)">St. Michaels, MD</div>
    <div class="tile" role="img" aria-label="White house with porch among trees" style="left:751px;top:32px;background:linear-gradient(180deg,#6e8c5a,#4a6a38 55%,#2e3a28)">Oxford, MD</div>
    <div class="tile" role="img" aria-label="Marina and lighthouse on the bay" style="left:195px;top:222px;background:linear-gradient(180deg,#3a5a8a,#5a7698 50%,#1f3454)">Cambridge, MD</div>
    <div class="tile" role="img" aria-label="Sailboats docked at an island marina" style="left:473px;top:222px;background:linear-gradient(180deg,#4a6ea0,#6d8aa8 50%,#23354e)">Tilghman Island, MD</div>
  </section>
  <div class="join" role="img" aria-label="Join our team panel over a darkened house photo">
    <h3>JOIN OUR TEAM</h3>
    <p>Become a part of our franchise with<br>exciting oppurtunity and growth</p>
    <span>Get In touch</span>
  </div>

  <main class="abs main"></main>
  <div class="intro">
    <h1>Ready To Discover Your<br>Next Fair Haven?</h1>
    <h4>Explore...Experience...Enjoy</h4>
    <div class="copy">
      <p>Lorem ipsum dolor sit amet, consectetuer adipiscing elit, sed diam nonummy nibh euismod tincidunt ut laoreet dolore magna aliquam erat volutpat. Ut wisi enim ad minim veniam, quis nostrud exerci tation ullamcorper suscipit lobortis nisl ut aliquip ex ea commodo consequat. Duis autem vel eum iriure dolor in hendrerit in vulputate velit esse molestie consequat, vel illum dolore eu feugiat nulla facilisis at vero eros et accumsan et iusto odio dignissim qui blandit praesent luptatum zzril delenit augue duis dolore te feugait nulla facilisi.</p>
      <p>Duis autem vel eum iriure dolor in hendrerit in vulputate velit esse molestie consequat, vel illum dolore eu feugiat nulla facilisis at vero eros et accumsan et iusto odio dignissim qui blandit praesent luptatum zzril delenit augue duis dolore te feugait nulla facilisi.</p>
      <p>Consectetuer adipiscing elit, sed diam nonummy nibh euismod tincidunt ut laoreet dolore magna aliquam erat volutpat. Ut wisi enim ad minim veniam, quis nostrud exerci tation ullamcorper suscipit lobortis nisl ut aliquip ex ea commodo consequat.</p>
    </div>
  </div>

  <div class="abs signup">Sign Up For Last Minute Gateway Deals!</div>
  <div class="abs email">Enter Your Email</div>
  <div class="abs btn">Sign me up!</div>

  <div class="card lift" style="top:754px;height:106px">
    <div class="ico"><svg width="26" height="34" viewBox="0 0 26 34"><path d="M13 2a11 11 0 0 0-11 11c0 8 11 19 11 19s11-11 11-19A11 11 0 0 0 13 2z" fill="none" stroke="#fff" stroke-width="4"/></svg></div>
    <h3>Know Of A Fair Haven?</h3>
    <p>Have you stayed in or own a property that may be a fair haven?</p>
    <a style="top:78px">Let Us Know About It!</a>
  </div>
  <div class="card" style="top:876px;height:141px">
    <div class="ico"><svg width="32" height="30" viewBox="0 0 32 30"><ellipse cx="16" cy="21" rx="8" ry="7" fill="#fff"/><circle cx="6" cy="12" r="3.5" fill="#fff"/><circle cx="26" cy="12" r="3.5" fill="#fff"/><circle cx="11" cy="5" r="3.5" fill="#fff"/><circle cx="21" cy="5" r="3.5" fill="#fff"/></svg></div>
    <h3>Pets <em>travel free!</em></h3>
    <p>We have a terrific selection of pet friendly vacation homes for you to choose from. Bring your pet along for <b>no additional charge!</b></p>
    <a style="top:113px">Find Out More</a>
  </div>
  <div class="card" style="top:1031px;height:106px">
    <div class="ico"><svg width="44" height="44" viewBox="0 0 44 44"><circle cx="22" cy="22" r="19" fill="none" stroke="#fff" stroke-width="3"/><path d="M22 11v12h9" fill="none" stroke="#fff" stroke-width="2.5"/></svg></div>
    <h3>Last Minute Deals</h3>
    <p>Duis autem vel eum iriure dolor in<br>hendrerit in vulputate velit .</p>
    <a style="top:78px">View Last Minute Deals</a>
  </div>

  <footer class="abs foot">
    <span class="bar" style="left:0;background:#4a90cf"></span>
    <span class="bar" style="left:285px;background:var(--green)"></span>
    <span class="bar" style="left:571px;background:#aaa"></span>
    <div class="col" style="left:22px"><h5>Fair Havens</h5>240 Harbor Lane<br>Bayview, MD<br>21699</div>
    <div class="col" style="left:307px"><h5>Contact Us</h5>1.855.FAIR.HVN<br>(1.855.324.7486)<br><u>info@fairhavens-stays.com</u></div>
    <div class="col" style="left:593px"><h5>Franchise Information</h5><u>About Fair Havens</u><br>Why a Fair Havens Franchise<br>FAQ</div>
  </footer>
  <div class="abs legal">
    Franchise information &nbsp;| &nbsp;Our Philosophy &nbsp;| &nbsp;List Your Properties &nbsp;| &nbsp;Contact Us &nbsp;| &nbsp;Site Map &nbsp;| &nbsp;Privacy Policy<br>Copyright 2014, Fair Havens
    <span class="dot" style="left:792px"></span>
    <span class="dot" style="left:818px"></span>
  </div>
</div>
</body>
</html>
```